TriVex Business Card Design - double sided -plumbing local plumbing company

We have a Plumbing company where the design was create through Sketch Hive. We would now like a business card designed as well. We want it to be in the colour version of the logo.

Details below for the card.

Phone Number: 0438 615 247
Email: info@trivexplumbing.example.au
Website: https://trivexplumbing.example.au
We really want a sophisticated design that stand out from the other- informative and timeless.

Target Market(s)

local Canberra market

Industry/Entity Type

Plumbing, gas fitting, hot water

Contact Information for Business Card

Phone number, email, logo and "Supplying all your heating, cooling and hot water needs"

Requirements
Must have
• bust be colourful, must also be though about it being printed on a magnet. must Vex with the logo - I dont want the logo and information chucked onto a white canvas I would prefer it to be smooth and look purposeful

```html
<!DOCTYPE html>
<html lang="en">
<head>
<meta charset="utf-8">
<title>TriVex Business Card</title>
<link rel="stylesheet" href="https://fonts.googleapis.com/css2?family=Montserrat:wght@400;500;700;800&display=swap">
<style>
  :root {
    --bg: #dcdcdc;
    --card-front: #ffffff;
    --card-back: #eeeeef;
    --blue: #22a7e0;
    --blue-deep: #0a9bd8;
    --orange: #f5a93f;
    --orange-deep: #e9a23c;
    --navy: #1f2b45;
    --shadow: rgba(0,0,0,0.18);
  }
  * { box-sizing: border-box; margin: 0; padding: 0; }
  html, body { width: 1200px; height: 1200px; overflow: hidden; }
  body {
    background: var(--bg);
    font-family: "Montserrat", sans-serif;
    color: var(--navy);
    position: relative;
  }
  .card {
    position: absolute;
    left: 160px;
    width: 880px;
    height: 503px;
    border-radius: 28px;
    box-shadow: 0 10px 28px var(--shadow);
    overflow: hidden;
  }
  .card--front { top: 70px; background: var(--card-front); }
  .card--back  { top: 625px; background: var(--card-back); }

  .brand {
    position: absolute;
    display: flex;
    align-items: center;
    gap: 18px;
    font-weight: 800;
    color: var(--blue);
    letter-spacing: 1px;
  }
  .brand__dot { border-radius: 50%; background: var(--orange); }
  .card--front .brand { left: 0; right: 0; top: 150px; justify-content: center; font-size: 118px; }
  .card--front .brand__dot { width: 70px; height: 70px; }
  .tagline {
    position: absolute; left: 0; right: 0; top: 370px;
    text-align: center; font-size: 25px; font-weight: 500; letter-spacing: 0.6px;
  }

  .card--back .brand { left: 72px; top: 62px; font-size: 70px; gap: 12px; }
  .card--back .brand__dot { width: 40px; height: 40px; }
  .person { position: absolute; right: 90px; top: 110px; text-align: right; }
  .person__name { font-size: 40px; font-weight: 800; color: var(--blue-deep); }
  .person__role { font-size: 24px; font-weight: 500; margin-top: 4px; }
  .area {
    position: absolute; left: 100px; top: 300px;
    font-size: 24px; font-weight: 500; line-height: 1.3; letter-spacing: 0.4px;
  }
  .contacts { position: absolute; left: 100px; top: 385px; list-style: none; }
  .contacts li {
    display: flex; align-items: center; gap: 14px;
    font-size: 24px; font-weight: 500; line-height: 34px; letter-spacing: 0.4px;
  }
  .contacts svg { width: 20px; height: 20px; flex: none; }
  .edge-band { position: absolute; right: 0; width: 22px; }
  .edge-band--top { top: 0; height: 180px; background: var(--blue-deep); border-bottom-left-radius: 12px; }
  .edge-band--mid { top: 200px; height: 80px; background: var(--orange-deep); border-radius: 12px 0 0 12px; }
  .edge-band--bottom { top: 300px; bottom: 0; background: var(--blue-deep); border-top-left-radius: 12px; }
</style>
</head>
<body>
  <section class="card card--front">
    <div class="brand"><span class="brand__name">TriVex</span><span class="brand__dot"></span></div>
    <p class="tagline">“Supplying all your heating, cooling and hot water needs”</p>
  </section>

  <section class="card card--back">
    <div class="brand"><span class="brand__name">TriVex</span><span class="brand__dot"></span></div>
    <div class="person">
      <p class="person__name">Marcus Keller</p>
      <p class="person__role">Founder &amp; Director</p>
    </div>
    <p class="area">Australia, Canberra and<br>surrounding areas</p>
    <ul class="contacts">
      <li>
        <svg viewBox="0 0 20 20" aria-hidden="true"><path fill="var(--blue)" d="M5 2l3 4-2 2c1 2.5 3.5 5 6 6l2-2 4 3-2 3C9 18 2 11 2 4z"/></svg>
        0438 615 247
      </li>
      <li>
        <svg viewBox="0 0 20 20" aria-hidden="true"><rect x="1" y="4" width="18" height="12" rx="1.5" fill="var(--blue)"/><path d="M2 5l8 6 8-6" fill="none" stroke="#fff" stroke-width="1.5"/></svg>
        info@trivexplumbing.example.au
      </li>
      <li>
        <svg viewBox="0 0 20 20" aria-hidden="true"><circle cx="10" cy="10" r="8.5" fill="var(--blue)"/><path d="M1.5 10h17M10 1.5v17M10 1.5c-4 4-4 13 0 17M10 1.5c4 4 4 13 0 17" fill="none" stroke="#fff" stroke-width="1.1"/></svg>
        www.trivexplumbing.example.au
      </li>
    </ul>
    <div class="edge-band edge-band--top"></div>
    <div class="edge-band edge-band--mid"></div>
    <div class="edge-band edge-band--bottom"></div>
  </section>
</body>
</html>
```